Updated flyer

we are a defence industry trainer and we are updating a course that has been running for a few years, so want a new look flyer. Please note that the flyer is A4 and we would like people to fill in the document online. Please add a tickbox for SME's free and add a call out box saying the course is NEW & UPDATED.

Industry/Entity Type

Defence

Font styles to use
Sans Serif
Other font styles liked:
• AVENIR

Colors
3176b5
01a88e
9bcb3b
fbed22
f37022

```html
<!DOCTYPE html>
<html lang="en">
<head>
<meta charset="utf-8">
<title>Defence, ITAR &amp; EAR Training Controls – Flyer</title>
<link href="https://fonts.googleapis.com/css2?family=Roboto+Condensed:wght@700;800&family=Nunito+Sans:wght@400;600;700;800&display=swap" rel="stylesheet">
<style>
:root{
  --blue:#3176b5;
  --blue-deep:#1f5596;
  --teal:#01a88e;
  --green:#4aa52a;
  --green-light:#9bcb3b;
  --yellow:#fbed22;
  --orange:#f37022;
  --price:#f6b52b;
  --grey-box:#e4e4e4;
  --grey-text:#555;
  --field:#b9b9b9;
  --ink:#111;
  --stage:#3b3b3d;
  --head:"Roboto Condensed",Arial,sans-serif;
  --body:"Nunito Sans",Arial,sans-serif;
}
*{box-sizing:border-box;margin:0;padding:0}
html,body{width:1200px;height:902px;overflow:hidden;background:var(--stage)}
body{position:relative;font-family:var(--body)}

.flyer{position:absolute;top:100px;width:514px;height:720px;background:#fff;overflow:hidden;box-shadow:0 4px 14px rgba(0,0,0,.45)}
.flyer--front{left:66px}
.flyer--back{left:624px}

.header-art{position:absolute;left:0;top:0;width:514px;height:160px}
.title{position:absolute;right:20px;top:14px;text-align:right;font-family:var(--head);font-weight:800;color:#fff;font-size:29px;line-height:32px;letter-spacing:.2px;white-space:nowrap}
.badge-new{position:absolute;right:22px;top:84px;font-family:var(--head);font-weight:800;color:var(--yellow);font-size:30px;letter-spacing:.8px}

.col-left{position:absolute;left:0;top:128px;width:252px;height:550px;background:#fff}
.col-right{position:absolute;left:252px;top:128px;width:262px;height:550px;background:linear-gradient(160deg,#58b52c 0%,var(--green) 55%,#3a9421 100%)}

.brand{position:absolute;left:18px;top:26px;display:flex;align-items:center;gap:12px}
.brand__dot{width:76px;height:76px;border-radius:50%;background:var(--green-light)}
.brand__name{font-family:var(--body);font-weight:700;color:var(--green);font-size:16px;line-height:18px;width:130px}

.quotes{position:absolute;left:0;top:148px;width:252px}
.quote{height:53px;margin-bottom:5px;background:var(--grey-box);display:flex;align-items:center;justify-content:center;text-align:center;color:var(--grey-text);font-size:15.5px;line-height:18px;padding:0 26px}
.quote b{font-family:Georgia,serif;font-size:22px;color:#444;line-height:0}

.dates{position:absolute;left:10px;top:438px;width:240px;height:112px;overflow:hidden;background:linear-gradient(var(--blue),var(--blue-deep));border-radius:12px 12px 0 0;text-align:center;color:#fff;padding-top:6px}
.dates h3{font-family:var(--head);font-weight:700;color:var(--yellow);font-size:18.5px;line-height:22px;margin-bottom:2px}
.dates p{font-size:15px;line-height:19.5px}

.pill{position:absolute;right:0;height:32px;background:var(--orange);border-radius:16px 0 0 16px;color:var(--yellow);font-family:var(--head);font-weight:700;font-size:22px;line-height:32px;text-align:right;padding-right:12px;box-shadow:0 2px 3px rgba(0,0,0,.25);white-space:nowrap}
.pill--about{top:60px;width:206px}

.about{position:absolute;left:12px;right:14px;top:104px;color:#fff;font-size:14.6px;line-height:19.6px;text-align:justify}
.about .hl{color:var(--yellow);font-weight:700}
.about .lead{display:block;text-align:right}
.price{position:absolute;right:14px;top:462px;text-align:right;font-family:var(--head);font-weight:700;color:var(--price);font-size:21px;white-space:nowrap}
.price small{display:block;font-family:var(--body);font-weight:600;font-size:12px}
.subsidy{position:absolute;left:12px;right:14px;top:506px;color:#fff;font-size:12.5px;line-height:16px;text-align:justify;text-align-last:center}

.footer{position:absolute;left:0;bottom:0;width:514px;height:42px;background:linear-gradient(#2a2a2a,#000);color:#fff;font-size:11.8px;line-height:42px;white-space:nowrap}
.footer--front{text-align:center}
.footer--front em{font-style:normal;color:var(--yellow);font-weight:700}
.footer--back{display:flex;align-items:center;justify-content:space-between;padding:0 22px;color:var(--yellow);font-weight:700}
.footer--back span{display:flex;align-items:center;gap:7px}
.footer svg{width:11px;height:11px;fill:#fff}

/* back */
.tab-register{position:absolute;left:0;top:126px;width:184px;height:28px;background:var(--orange);border-radius:0 14px 14px 0;color:var(--yellow);font-family:var(--head);font-weight:700;font-size:16px;line-height:28px;padding-left:8px;white-space:nowrap}
.form{position:absolute;left:8px;top:164px;width:236px;font-size:8px;color:#333}
.form__row{display:flex;align-items:center;height:11.6px}
.form__row label{width:56px;white-space:nowrap}
.form__row i{flex:1;height:9.5px;background:var(--field)}
.form__pay{font-size:6.2px;line-height:9px;margin:4px 0 2px;color:#333;white-space:nowrap}
.form__pay span{display:inline-block;margin-right:10px}
.box{display:inline-block;width:5px;height:5px;border:.6px solid #555;margin-right:3px;vertical-align:middle}
.form__row--card label{width:60px;font-size:6.2px}
.form__row--card{height:12px}
.form__row--card i{height:9px}

.register{position:absolute;left:12px;top:330px;color:#333;white-space:nowrap}
.register h3{font-family:var(--body);font-weight:800;color:var(--blue-deep);font-size:19px;margin-bottom:4px}
.register p{font-size:12.8px;line-height:20.5px;display:flex;align-items:center;gap:8px}
.register svg{width:10px;height:10px;fill:var(--orange)}

.office{position:absolute;left:10px;top:427px;width:240px;height:123px;background:linear-gradient(var(--blue),var(--blue-deep));border-radius:12px 12px 0 0;padding:8px 10px;color:#fff}
.office h3{font-family:var(--head);font-weight:700;color:var(--yellow);font-size:19px;margin-bottom:6px}
.office p{display:flex;font-size:8.8px;height:22px;align-items:center}
.office p span{width:84px}
.office p i{flex:1;border-bottom:1px dotted #fff;height:6px}

.pill--content{top:58px;width:210px;font-size:19px}
.topics{position:absolute;right:10px;top:96px;width:250px;list-style:none;color:#fff;font-size:7.9px;line-height:11.2px;text-align:right}
.topics li::after{content:"";display:inline-block;width:4px;height:4px;border-radius:50%;background:var(--yellow);margin-left:6px;vertical-align:middle}
.pill--cancel{top:434px;width:210px;font-size:20px}
.cancel{position:absolute;right:14px;left:16px;top:472px;color:#fff;font-size:11.8px;line-height:14.6px;text-align:right}
</style>
</head>
<body>

<!-- Front side -->
<section class="flyer flyer--front">
  <div class="col-left">
    <div class="brand"><span class="brand__dot"></span><span class="brand__name">Meridian Trade Compliance Institute</span></div>
    <div class="quotes">
      <p class="quote"><span><b>“</b>Excellent structure and style of presentation.<b>”</b></span></p>
      <p class="quote"><span><b>“</b>Excellent...best U.S export controls training I have attended.”</span></p>
      <p class="quote"><span><b>“</b>Practical workshops were fantastic.<b>”</b></span></p>
      <p class="quote"><span><b>“</b>Excellent presenter and coordination.<b>”</b></span></p>
      <p class="quote"><span><b>“</b>Very informative, well presented course.<b>”</b></span></p>
    </div>
    <div class="dates">
      <h3>Check Out Dates &amp; Places</h3>
      <p>Brisbane 16 &amp; 17 March<br>Sydney 18 &amp; 19 March<br>Canberra 20 &amp; 23 March<br>Melbourne 24 &amp; 25 March</p>
    </div>
  </div>
  <div class="col-right">
    <div class="pill pill--about">About Training</div>
    <p class="about"><span class="hl lead">U.S. Export Controls</span>are some of the most complex and stringent in the world. The U.S. Government regulates the transfer of U.S. origin goods and technical data throughout the world, with the intent of preventing unauthorised transfer of technology and know-how. These controls extend world-wide and can impact anyone dealing in U.S. controlled goods or technology. <span class="hl">This two-day comprehensive course</span> will give applicants a greater understanding of U.S. Export Controls from a non-U.S. perspective in practical and relevant terms.</p>
    <p class="price">$1295.00 AUD per person<small>inc GST</small></p>
    <p class="subsidy">Subsidised by the Defence Sector Skills Fund (DSSF)</p>
  </div>
  <svg class="header-art" viewBox="0 0 514 160" aria-hidden="true">
    <defs><linearGradient id="hdrA" x1="0" y1="0" x2="0" y2="1"><stop offset="0" stop-color="#2c6db0"/><stop offset="1" stop-color="#1c4f8e"/></linearGradient></defs>
    <path d="M0 0H514V150C440 132 360 122 262 128C170 132 80 120 0 112Z" fill="url(#hdrA)"/>
    <path d="M0 112C80 120 170 132 262 128C190 132 100 128 0 136Z" fill="#f37022"/>
  </svg>
  <h1 class="title">Defence ,ITAR &amp; EAR Training Controls<br>from a non-U.S. Perspective Training</h1>
  <p class="badge-new">NEW UPDATED</p>
  <footer class="footer footer--front">For more information, please contact MTCI on <em>+61 (0)7 5550 0142</em> or <em>info@mtci.org</em></footer>
</section>

<!-- Back side -->
<section class="flyer flyer--back">
  <div class="col-left">
    <div class="brand"><span class="brand__dot"></span><span class="brand__name">Meridian Trade Compliance Institute</span></div>
    <div class="tab-register">Register Online or below</div>
    <div class="form">
      <div class="form__row"><label>Name:</label><i></i></div>
      <div class="form__row"><label>Company:</label><i></i></div>
      <div class="form__row"><label>Address:</label><i></i></div>
      <div class="form__row"><label>Mobile no:</label><i></i></div>
      <div class="form__row"><label>Email:</label><i></i></div>
      <div class="form__row"><label>Dietary needs:</label><i></i></div>
      <p class="form__pay">Payment method: (please check one)<br>
        <span><i class="box"></i>Invoice</span><span style="margin-left:40px"><i class="box"></i>Free of Charge (SME)</span><br>
        <span><i class="box"></i>Credit card*</span><br>
        <span>Card type:</span><span><i class="box"></i>Debit</span><span><i class="box"></i>Credit</span><span><i class="box"></i>Charge</span></p>
      <div class="form__row form__row--card"><label>Card name:</label><i></i></div>
      <div class="form__row form__row--card"><label>Card number:</label><i></i></div>
      <div class="form__row form__row--card"><label>Expiry date:</label><i></i></div>
      <div class="form__row form__row--card"><label>Cardholder email:</label><i></i></div>
    </div>
    <div class="register">
      <h3>Register online @</h3>
      <p><svg viewBox="0 0 10 10"><circle cx="5" cy="5" r="4"/></svg>learn-compliance.online/events</p>
      <p><svg viewBox="0 0 10 10"><path d="M0 2H10V8H0Z M0 2L5 6L10 2" stroke="#fff" stroke-width=".8"/></svg>registrations to enrol@mtci.org</p>
      <p><svg viewBox="0 0 10 10"><path d="M1 3C1 1 3 1 5 1S9 1 9 3L7 4L6 3H4L3 4Z M2 5H8L9 9H1Z"/></svg>+61 (0)7 5550 0187</p>
    </div>
    <div class="office">
      <h3>OFFICE USE ONLY</h3>
      <p><span>Confirmation sent</span><i></i></p>
      <p><span>Invoice no</span><i></i></p>
      <p><span>Contact person</span><i></i></p>
      <p><span>Paid</span><i></i></p>
    </div>
  </div>
  <div class="col-right">
    <div class="pill pill--content">2 Day Course Content</div>
    <ul class="topics">
      <li>Export Control terms and conditions</li>
      <li>Export Control Reform and the impact to Australian industry</li>
      <li>Managing reclassifications</li>
      <li>Applying de minimis</li>
      <li>Understanding 600 Series &amp; limitations</li>
      <li>Understanding the Commerce Country List, Country<br>Chart &amp; Country Groups</li>
      <li>Understanding deemed exports</li>
      <li>EAR General Prohibitions</li>
      <li>U.S. export controls jurisdictions</li>
      <li>Relevant legislation</li>
      <li>Understand U.S. authorisations</li>
      <li>Sub-licensing options &amp; requirements</li>
      <li>Applying U.S. exemptions</li>
      <li>Understanding re-exports &amp; how to obtain authorisation</li>
      <li>Australian export controls</li>
      <li>Australian / U.S. Trade Co-operation Treaty</li>
      <li>Dual &amp; third country national issues &amp; exemptions</li>
      <li>Developing a compliance framework</li>
      <li>Cloud Computing &amp; other technical issues</li>
      <li>Managing multi-jurisdictions</li>
      <li>Identifying the best authorisations to use</li>
      <li>Record-keeping &amp; administrative requirements</li>
      <li>Understanding FMS</li>
      <li>Creating a monitoring &amp; self-assessment process</li>
      <li>Managing violations</li>
      <li>Non-compliance &amp; fines</li>
    </ul>
    <div class="pill pill--cancel">Cancellation Policy</div>
    <p class="cancel">Cancellations incur a 20% administration fee. No cancellations permitted within 30 days of training commencing. If a registered attendee is unable to attend, a replacement attendee is allowed.</p>
  </div>
  <svg class="header-art" viewBox="0 0 514 160" aria-hidden="true">
    <defs><linearGradient id="hdrB" x1="0" y1="0" x2="0" y2="1"><stop offset="0" stop-color="#2c6db0"/><stop offset="1" stop-color="#1c4f8e"/></linearGradient></defs>
    <path d="M0 0H514V150C440 132 360 122 262 128C170 132 80 120 0 112Z" fill="url(#hdrB)"/>
    <path d="M0 112C80 120 170 132 262 128C190 132 100 128 0 136Z" fill="#f37022"/>
  </svg>
  <h1 class="title">Defence ,ITAR &amp; EAR Training Controls<br>from a non-U.S. Perspective Training</h1>
  <p class="badge-new">NEW UPDATED</p>
  <footer class="footer footer--back">
    <span><svg viewBox="0 0 10 10"><path d="M1 3C1 1 3 1 5 1S9 1 9 3L7 4L6 3H4L3 4Z M2 5H8L9 9H1Z"/></svg>+61 (0)7 5550 0142</span>
    <span><svg viewBox="0 0 10 10"><circle cx="5" cy="5" r="4.5"/></svg>www.mtci.org</span>
    <span><svg viewBox="0 0 10 10"><path d="M0 2H10V8H0Z"/></svg>info@mtci.org</span>
  </footer>
</section>

</body>
</html>
```